Design of a Web Development Agency

We're a web development agency (we do not offer design services). We'd like to get a new website up and running. We do custom web application development - large scale applications in the financial, healthcare, automotive, and other industries.

We need the following types of pages designed:
1) Homepage
2) Blog
3) Services page
4) Packages page
4) Generic content
5) Contact Us form.

The design should be consistent with our current icon. We're looking for a clean, corporate, brand. We'd like the design to expand on the concepts in the logo - the use of the electrical wiring motif / the colors / etc.

We offer the following services: 1) Cobalto web hosting consulting, 2) custom application development, 3) Qel development, 4) Veltrix development.

We offer packages in numbers of hours. We have about 3-4 tiers of services - the number of hours versus the monthly invoice total. For example, 5 hours per month of $500.00, for example.

Target Market(s)

Corporate clients

Industry/Entity Type

Electrical

Colors
acd036
33b7a4
33a6d7
3176b5
876aae
b768aa
fbee3e

Requirements
Must have
• Responsive / mobile friendly design.
• An email submitting form on the contact us page
Nice to have
• We'd like a bit of San Francisco to come through (where we're located)
• A plorvo map of our address on the contact us page
Should not have
• Excessive imagery. We don't have a lot of imagery, so we'd basically have to go out and find stock photography to put in it's place, which we just don't really want to do. All imagery should be supplied by the designer (we'll pay any copyright fees, if applicable, you just have to send us a list of the links to the imagery. Max budget would be $100-$200 on imagery, but preferably as little as possible).

```html
<!DOCTYPE html>
<html lang="en">
<head>
<meta charset="utf-8">
<title>Halden Web Works — Custom Web Application Development</title>
<link rel="stylesheet" href="https://fonts.googleapis.com/css2?family=Source+Sans+3:wght@300;400;600;700&family=Open+Sans:wght@300;400;600&family=Alegreya+Sans+SC:wght@300;400&display=swap">
<style>
  :root {
    --lime: #acd036;
    --lime-dark: #98bb22;
    --teal: #33b7a4;
    --sky: #33a6d7;
    --blue: #3176b5;
    --purple: #876aae;
    --pink: #b768aa;
    --ink: #222222;
    --text: #555555;
    --muted: #8a8a8a;
    --rule: #e4e4e4;
    --card-tint: #f5f6f8;
    --slate: #3b4045;
    --slate-deep: #2b2f33;
    --olive: #78981c;
    --footer: #1b1b1b;
    --white: #ffffff;
  }
  * { box-sizing: border-box; margin: 0; padding: 0; }
  html, body { width: 1200px; height: 2446px; overflow: hidden; }
  body {
    position: relative;
    background: var(--white);
    font-family: "Source Sans 3", "Helvetica Neue", Arial, sans-serif;
    color: var(--text);
  }

  /* Header */
  .site-header { position: absolute; top: 0; left: 0; width: 1200px; height: 106px; background: var(--white); }
  .brand { position: absolute; left: 101px; top: 27px; display: flex; align-items: center; gap: 14px; }
  .brand-dot { width: 52px; height: 52px; border-radius: 50%; background: var(--lime); }
  .brand-name { font-family: "Source Sans 3", sans-serif; font-weight: 700; font-size: 20px; color: var(--ink); letter-spacing: .2px; }
  .main-nav { position: absolute; left: 484px; top: 0; display: flex; height: 106px; }
  .main-nav a { display: flex; align-items: center; padding: 0 18px; height: 106px; font-family: "Open Sans", sans-serif; font-size: 15px; color: var(--ink); text-decoration: none; }
  .main-nav a.is-active { background: var(--lime); padding: 0 15px; }

  /* Hero */
  .hero { position: absolute; top: 106px; left: 0; width: 1200px; height: 437px; }
  .hero-photo { position: absolute; inset: 0; background:
      radial-gradient(ellipse 260px 340px at 390px 230px, #6e6a66 0%, rgba(90,86,82,.6) 45%, rgba(40,40,40,0) 100%),
      linear-gradient(90deg, #2c2c2c 0%, #4a4a48 35%, #3a3a3a 60%, #1e1e1e 100%); }
  .hero-copy { position: absolute; left: 560px; top: 82px; width: 520px; color: var(--white); }
  .hero-title { font-family: "Open Sans", sans-serif; font-weight: 400; font-size: 32px; line-height: 44px; text-align: center; width: 510px; margin-left: -2px; text-transform: uppercase; letter-spacing: .5px; }
  .hero-lead { margin-top: 8px; font-family: "Open Sans", sans-serif; font-size: 23px; line-height: 30px; text-align: right; width: 511px; }
  .hero-actions { position: absolute; left: 615px; top: 293px; display: flex; }
  .btn-hero { width: 200px; height: 51px; display: flex; align-items: center; justify-content: center; color: var(--white); font-size: 18px; text-transform: uppercase; font-family: "Source Sans 3", sans-serif; letter-spacing: .3px; }
  .btn-hero.start { background: var(--teal); }
  .btn-hero.learn { background: var(--blue); width: 205px; }
  .hero-or { position: absolute; left: 184px; top: 9px; width: 33px; height: 33px; border-radius: 50%; background: #c9c9c9; border: 3px solid #e8e8e8; color: var(--white); font-size: 10px; display: flex; align-items: center; justify-content: center; }

  /* Industry band */
  .industry-band { position: absolute; top: 543px; left: 0; width: 1200px; height: 91px; background: var(--lime); display: flex; align-items: center; justify-content: center; }
  .industry-band p { font-family: "Open Sans", sans-serif; font-size: 19px; color: var(--ink); text-transform: uppercase; letter-spacing: .2px; }
  .industry-band span { color: var(--white); }

  /* Section headings */
  .section-title { position: absolute; left: 0; width: 1200px; text-align: center; font-family: "Open Sans", sans-serif; font-weight: 300; font-size: 26px; color: #4a4a4a; text-transform: uppercase; letter-spacing: .5px; }
  .section-title small { font-size: 13px; color: var(--muted); letter-spacing: .5px; }
  .soft-rule { position: absolute; left: 260px; width: 680px; height: 1px; background: linear-gradient(90deg, rgba(0,0,0,0), #e6e6e6 50%, rgba(0,0,0,0)); }

  /* Services */
  .services-art { position: absolute; left: 98px; top: 708px; width: 660px; height: 400px; border-radius: 6px;
    background: radial-gradient(ellipse 330px 200px at 420px 220px, #e8e8e8 0%, #f2f2f2 55%, rgba(255,255,255,0) 100%); }
  .service { position: absolute; display: flex; gap: 14px; align-items: flex-start; }
  .service-icon { flex: none; width: 72px; height: 72px; border-radius: 50%; border: 5px solid #eeeeee; display: flex; align-items: center; justify-content: center; box-shadow: 0 1px 3px rgba(0,0,0,.15); }
  .service-icon.hosting { background: var(--purple); }
  .service-icon.custom { background: var(--blue); }
  .service-icon.qel { background: var(--pink); }
  .service-icon.veltrix { background: var(--lime); }
  .service-body { width: 300px; padding-top: 2px; }
  .service-body h3 { font-weight: 400; font-size: 14.5px; color: #666; text-transform: uppercase; letter-spacing: .2px; }
  .service-body p { font-size: 13px; line-height: 18px; color: #777; margin-top: 3px; }

  /* Packages */
  .package { position: absolute; background: var(--white); border: 1px solid #e2e2e2; box-shadow: 0 1px 4px rgba(0,0,0,.08); text-align: center; }
  .package-name { height: 47px; line-height: 47px; font-weight: 600; font-size: 15.5px; color: #444; letter-spacing: .3px; }
  .package-price { position: relative; height: 82px; background: var(--card-tint); border-top: 1px solid #ececec; border-bottom: 1px solid #ececec; }
  .package-price .amount { position: absolute; left: 58px; top: 16px; font-weight: 300; font-size: 44px; line-height: 50px; }
  .package-price .hours { position: absolute; right: 12px; top: 10px; font-size: 13px; }
  .package-desc { font-size: 12.5px; line-height: 18px; color: #666; padding: 20px 30px 0; height: 76px; }
  .package-star { height: 22px; border-bottom: 1px solid var(--rule); margin: 0 16px; color: #cfcfcf; font-size: 15px; line-height: 16px; }
  .package-features { list-style: none; margin: 0 16px; }
  .package-features li { height: 34px; line-height: 34px; font-size: 12px; color: #555; border-bottom: 1px solid var(--rule); }
  .package-features li:last-child { border-bottom: 0; }
  .package-foot { position: absolute; left: 0; bottom: 0; width: 100%; height: 78px; border-top: 1px solid #ececec; display: flex; align-items: center; justify-content: center; }
  .package-btn { width: 170px; height: 41px; line-height: 41px; color: var(--white); font-size: 14px; }
  .package.basic .amount, .package.basic .hours { color: var(--teal); }
  .package.basic .package-btn { background: var(--teal); }
  .package.plus .amount, .package.plus .hours { color: var(--purple); }
  .package.plus .package-btn { background: var(--purple); }
  .package.premium .amount, .package.premium .hours { color: var(--sky); }
  .package.premium .package-btn { background: var(--sky); }
  .package.advanced { background: var(--slate); border-color: #2c3034; }
  .package.advanced .package-name { background: var(--slate-deep); color: var(--white); height: 50px; line-height: 50px; font-weight: 700; font-size: 16px; }
  .package.advanced .package-price { background: var(--slate-deep); border: 0; height: 82px; }
  .package.advanced .amount { left: 60px; top: 20px; color: var(--lime); }
  .package.advanced .hours { color: var(--lime); top: 4px; }
  .package.advanced .package-desc { color: #e4e4e4; padding-top: 22px; height: 68px; }
  .package.advanced .package-star { color: var(--white); border-color: #4d5359; }
  .package.advanced .package-features li { color: #e6e6e6; border-color: #4d5359; }
  .package.advanced .package-foot { background: var(--slate-deep); border-top: 0; height: 84px; }
  .package.advanced .package-btn { background: var(--lime); }
  .ribbon { position: absolute; right: 0; top: 0; width: 32px; height: 32px; background: var(--lime-dark); }

  /* About & blogs */
  .block-title { font-family: "Alegreya Sans SC", sans-serif; font-weight: 300; font-size: 31px; color: #333; }
  .about { position: absolute; left: 101px; top: 1915px; width: 600px; }
  .about .lead { margin-top: 9px; font-size: 14.5px; line-height: 20px; color: var(--olive); }
  .about .body { margin-top: 8px; font-size: 14.5px; line-height: 20px; color: #555; }
  .blogs { position: absolute; left: 730px; top: 1915px; width: 372px; }
  .blog-post { padding: 12px 0 18px; border-bottom: 1px solid var(--rule); }
  .blog-post:last-child { border-bottom: 0; padding-top: 24px; }
  .blog-post h4 { font-weight: 400; font-size: 14.5px; color: var(--olive); }
  .blog-post p { margin-top: 12px; font-size: 14.5px; line-height: 20px; color: #555; }

  /* Footer */
  .site-footer { position: absolute; left: 0; top: 2334px; width: 1200px; height: 112px; background: var(--footer); }
  .copyright { position: absolute; left: 111px; top: 46px; font-size: 13.5px; color: #e6e6e6; }
  .footer-divider { position: absolute; left: 481px; top: 28px; height: 56px; border-left: 1px dotted #666; }
  .social { position: absolute; left: 504px; top: 41px; display: flex; gap: 12px; }
  .social span { width: 28px; height: 28px; border-radius: 50%; }
  .social .s1 { background: #2f5b9a; }
  .social .s2 { background: #2ea6e0; }
  .social .s3 { background: #f29a1d; }
  .social .s4 { background: #a8a8a8; }
  .footer-brand { position: absolute; left: 851px; top: 30px; display: flex; align-items: center; gap: 14px; }
  .footer-brand .brand-dot { width: 50px; height: 50px; background: #4a4a4a; }
  .footer-brand .brand-name { font-weight: 400; color: #9a9a9a; font-size: 17px; }
</style>
</head>
<body>

<header class="site-header">
  <div class="brand">
    <span class="brand-dot"></span>
    <span class="brand-name">HALDEN WEB WORKS</span>
  </div>
  <nav class="main-nav">
    <a class="is-active" href="#">Home</a>
    <a href="#">Blog</a>
    <a href="#">Services</a>
    <a href="#">Packages</a>
    <a href="#">Generic content</a>
    <a href="#">Contact Us</a>
  </nav>
</header>

<section class="hero">
  <div class="hero-photo" role="img" aria-label="Hand holding a smartphone showing a social feed, over a blurred dark office background"></div>
  <div class="hero-copy">
    <h1 class="hero-title">Custom Web Application /<br>Development</h1>
    <p class="hero-lead">You download awesome music. So do cool,<br>sexy, fun people in your city. Find them.</p>
  </div>
  <div class="hero-actions">
    <a class="btn-hero start">Get Started</a>
    <a class="btn-hero learn">Learn More</a>
    <span class="hero-or">OR</span>
  </div>
</section>

<div class="industry-band">
  <p>Large scale applications <span>in the financial,</span> healthcare<span>, automotive, and</span> other industries</p>
</div>

<h2 class="section-title" style="top:665px">Our Services</h2>
<div class="services-art" role="img" aria-label="Laptop showing a dashboard, surrounded by faint speech bubbles and social icons"></div>

<div class="service" style="left:649px; top:714px">
  <div class="service-icon hosting">
    <svg width="34" height="30" viewBox="0 0 34 30" fill="none" stroke="#fff" stroke-width="2"><path d="M10 12a6 6 0 0 1 12-2a5 5 0 0 1 2 10H10a4 4 0 0 1 0-8z"/><path d="M17 20v4M6 26h22"/></svg>
  </div>
  <div class="service-body"><h3>Cobalto web hosting consulting</h3><p>simply dummy text of the printing and typesetting industry. Lorem Ipsum has been the industry's</p></div>
</div>
<div class="service" style="left:761px; top:807px">
  <div class="service-icon custom">
    <svg width="30" height="24" viewBox="0 0 30 24" fill="none" stroke="#fff" stroke-width="2.6" stroke-linecap="round"><path d="M9 5L3 12l6 7M21 5l6 7-6 7M17 3l-4 18"/></svg>
  </div>
  <div class="service-body" style="padding-top:0"><h3>Custom app development</h3><p>simply dummy text of the printing and typesetting industry. Lorem Ipsum has been the industry's</p></div>
</div>
<div class="service" style="left:764px; top:916px">
  <div class="service-icon qel">
    <svg width="20" height="32" viewBox="0 0 20 32" fill="none" stroke="#fff" stroke-width="2"><rect x="2" y="2" width="16" height="28" rx="3"/><circle cx="10" cy="25" r="1.5" fill="#fff"/></svg>
  </div>
  <div class="service-body" style="padding-top:0"><h3>Qel development</h3><p>simply dummy text of the printing and typesetting industry. Lorem Ipsum has been the industry's</p></div>
</div>
<div class="service" style="left:676px; top:1017px">
  <div class="service-icon veltrix">
    <svg width="20" height="32" viewBox="0 0 20 32" fill="none" stroke="#fff" stroke-width="2"><rect x="2" y="2" width="16" height="28" rx="3"/><path d="M7 26h6"/></svg>
  </div>
  <div class="service-body" style="padding-top:10px"><h3>Veltrix development</h3><p>simply dummy text of the printing and typesetting industry. Lorem Ipsum has been the industry's</p></div>
</div>

<div class="soft-rule" style="top:1157px"></div>

<h2 class="section-title" style="top:1206px">Our Packages<small> ( In numbers of hours )</small></h2>

<article class="package basic" style="left:103px; top:1320px; width:228px; height:436px">
  <h3 class="package-name">Basic Package</h3>
  <div class="package-price"><span class="amount">$500</span><span class="hours">5 hrs / month</span></div>
  <p class="package-desc">Everything you need to start developing a new site</p>
  <div class="package-star">★</div>
  <ul class="package-features"><li>2 CPUS</li><li>768MB RAM</li><li>50GB Disk Space</li><li>Weekly Backups</li></ul>
  <div class="package-foot"><a class="package-btn">Learn more...</a></div>
</article>

<article class="package plus" style="left:357px; top:1320px; width:228px; height:436px">
  <h3 class="package-name">Plus Package</h3>
  <div class="package-price"><span class="amount">$600</span><span class="hours">6 hrs / month</span></div>
  <p class="package-desc">Everything you need to start developing a new site</p>
  <div class="package-star">★</div>
  <ul class="package-features"><li>2 CPUS</li><li>768MB RAM</li><li>50GB Disk Space</li><li>Weekly Backups</li></ul>
  <div class="package-foot"><a class="package-btn">Learn more...</a></div>
</article>

<article class="package advanced" style="left:611px; top:1296px; width:229px; height:489px">
  <h3 class="package-name">Advanced Package</h3>
  <span class="ribbon"><svg width="32" height="32" viewBox="0 0 32 32"><path d="M16 7l2.4 5 5.4.6-4 3.7 1.1 5.4L16 19l-4.9 2.7 1.1-5.4-4-3.7 5.4-.6z" fill="#fff"/></svg></span>
  <div class="package-price"><span class="amount">$600</span><span class="hours">6 hrs / month</span></div>
  <p class="package-desc">Everything you need to start developing a new site.</p>
  <div class="package-star">★</div>
  <ul class="package-features"><li>2 CPUS</li><li>768MB RAM</li><li>50GB Disk Space</li><li>150GB Bandwidth</li><li>Weekly Backups</li></ul>
  <div class="package-foot"><a class="package-btn">Learn more...</a></div>
</article>

<article class="package premium" style="left:866px; top:1322px; width:228px; height:434px">
  <h3 class="package-name">Premium Package</h3>
  <div class="package-price"><span class="amount">$900</span><span class="hours">9 hrs / month</span></div>
  <p class="package-desc">Everything you need to start developing a new site.</p>
  <div class="package-star">★</div>
  <ul class="package-features"><li>2 CPUS</li><li>768MB RAM</li><li>50GB Disk Space</li><li>Weekly Backups</li></ul>
  <div class="package-foot"><a class="package-btn">Learn more...</a></div>
</article>

<div class="soft-rule" style="top:1860px"></div>

<section class="about">
  <h2 class="block-title">About Us</h2>
  <p class="lead">consectetur adipisicing elit, sed do eiusmod tempor incididunt ut labore et dolore magna aliqua. Ut enim ad minim veniam, quis nostrud exercitation ullamco laboris nisi ut aliquip ex ea commodo consequat. Duis aute irure dolor in reprehenderit in voluptate velit esse</p>
  <p class="body">consectetur adipisicing elit, sed do eiusmod tempor incididunt ut labore et dolore magna aliqua. Ut enim ad minim veniam, quis nostrud exercitation ullamco laboris nisi ut aliquip ex ea commodo consequat. Duis aute irure dolor in reprehenderit in voluptate velit esse cillum dolore eu fugiat nulla pariatur. Excepteur sint occaecat cupidatat non proident, sunt in culpa qui officia deserunt mollit anim id est laborum Duis aute irure dUt enim ad minim veniam, quis nostrud exercitation ullamco laboris nisi ut aliquip ex ea commodo consequat. Duis aute irure dolor in reprehenderit in voluptate velit esse cillum dolore eu fugiat nulla pariatur. Excepteur sint occaecat cupidatat non proident, sunt in culpa qui officia deserunt mollit anim id est laborum Duis aute irure dolor in reprehenderit in voluptate.olor in reprehenderit in voluptate.</p>
</section>

<section class="blogs">
  <h2 class="block-title">Latest Blogs</h2>
  <article class="blog-post">
    <h4>Lorem ipsum dolor sit amet</h4>
    <p>Simply dummy text of the printing and typesetting industry. Lorem Ipsum has been the simply dummy text of the printing and typesetting industry.simply dummy text of the printing and typesetting industry. Lorem Ipsum has</p>
  </article>
  <article class="blog-post">
    <h4>Lorem ipsum dolor sit amet</h4>
    <p>Simply dummy text of the printing and typesetting industry. Lorem Ipsum has been the simply dummy text of the printing and typesetting industry.simply dummy text of the printing and typesetting industry. Lorem Ipsum has</p>
  </article>
</section>

<footer class="site-footer">
  <p class="copyright">Copyright © Halden web works 2014.&nbsp; All Rights Reserved</p>
  <span class="footer-divider"></span>
  <div class="social"><span class="s1"></span><span class="s2"></span><span class="s3"></span><span class="s4"></span></div>
  <div class="footer-brand">
    <span class="brand-dot"></span>
    <span class="brand-name">HALDEN WEB WORKS</span>
  </div>
</footer>

</body>
</html>
```